Gutschein Design Weihnachtsaktion Mähroboter
Zielgruppe
Installation für Mähroboter
Aufgabenstellung
Format DIN Lang (99x120mm) quer
Gutschein zur Installation eines Mähroboters
Auswahlfelder: für oberirdische oder unterirdische Verlegung
Auswahlfelder: bis 250m²; bis 500m², bis 1.000m²
Adressfeld/Namensfeld für den beschenkten
Serienfeld für Gutscheinnummer
Datums und Unterschriftsfeld
Design Vorstellung: Ein Männchen welches einen Mähroboter installiert, Design Mähroboter mit Weihnachtsmütze.... / Weihnachtliche Grundgestaltung. Sind für Ideen offen!
unser Logo integrieren

```html
<!DOCTYPE html>
<html lang="de">
<head>
<meta charset="utf-8">
<title>Mähroboter Installation Gutschein</title>
<link href="https://fonts.googleapis.com/css2?family=Roboto:wght@300;400;500&display=swap" rel="stylesheet">
<style>
  :root {
    --wood-dark: #2a1810;
    --wood-mid: #5a3522;
    --wood-light: #7a4c30;
    --panel: #ffffff;
    --ink: #2b2b2b;
    --line: #333333;
    --accent: #ee7b22;
    --title: #ffffff;
  }
  * { margin: 0; padding: 0; box-sizing: border-box; }
  html, body { width: 1200px; height: 990px; overflow: hidden; }
  body { font-family: "Roboto", Arial, sans-serif; font-weight: 300; color: var(--ink); }

  .voucher {
    position: relative; width: 1200px; height: 990px; overflow: hidden;
    background: radial-gradient(ellipse at 55% 25%, var(--wood-light) 0%, var(--wood-mid) 45%, var(--wood-dark) 100%);
  }
  .scene-left, .scene-right { position: absolute; top: 180px; width: 90px; height: 700px; }
  .scene-left { left: 0; background: linear-gradient(90deg, #2f4a22, rgba(47,74,34,0)); }
  .scene-right { right: 0; background: linear-gradient(270deg, #34502a, rgba(52,80,42,0)); }
  .table-edge { position: absolute; left: 0; right: 0; bottom: 0; height: 120px;
    background: linear-gradient(180deg, #4a2b1a, #2a170d); }

  .robot-photo {
    position: absolute; left: 102px; top: 59px; width: 424px; height: 260px;
    border-radius: 12px;
    background: linear-gradient(160deg, rgba(42,150,138,0.55) 0%, rgba(30,110,102,0.45) 55%, rgba(60,50,45,0.35) 100%);
  }

  .title { position: absolute; right: 63px; text-align: right; color: var(--title); font-weight: 300; line-height: 1; }
  .title-line { top: 70px; font-size: 54px; letter-spacing: 0.5px; }
  .title-main { top: 125px; font-size: 112px; letter-spacing: 0.5px; }

  .form-panel {
    position: absolute; left: 59px; top: 319px; width: 1077px; height: 632px;
    background: var(--panel);
  }
  .label, .option, .contact { position: absolute; font-size: 22px; white-space: nowrap; line-height: 1; }
  .field { position: absolute; border: 1.5px solid var(--line); height: 39px; }
  .checkbox { position: absolute; width: 21px; height: 21px; border: 1.5px solid var(--line); }
  .signline { position: absolute; height: 0; border-top: 1.5px solid var(--line); }

  .brand { position: absolute; left: 80px; top: 878px; display: flex; align-items: center; gap: 10px; }
  .brand-dot { width: 22px; height: 22px; border-radius: 50%; background: var(--accent); }
  .brand-name { font-size: 20px; font-weight: 500; color: var(--accent); white-space: nowrap; }

  .contact-line { left: 315px; top: 858px; font-size: 26px; }
  .contact-web { left: 315px; top: 896px; font-size: 26px; font-weight: 500; color: var(--accent); }
</style>
</head>
<body>
<main class="voucher">
  <div class="scene-left" role="img" aria-label="Tannenzweige mit roten Christbaumkugeln"></div>
  <div class="scene-right" role="img" aria-label="Tannenzweige und Weihnachtsgebäck"></div>
  <div class="table-edge" role="img" aria-label="Holztisch"></div>

  <div class="robot-photo" role="img" aria-label="Foto: türkisfarbener Mähroboter mit Weihnachtsmütze auf Ladestation"></div>

  <h2 class="title title-line">Mähroboter Installation</h2>
  <h1 class="title title-main">Gutschein</h1>

  <section class="form-panel"></section>

  <span class="label" style="left:103px; top:363px;">Modell:</span>
  <div class="field" style="left:334px; top:354px; width:202px;"></div>
  <span class="label" style="left:848px; top:363px;">Gutschein Nr.:</span>

  <span class="label" style="left:103px; top:430px;">Name, Vorname:</span>
  <div class="field" style="left:334px; top:422px; width:766px;"></div>

  <span class="label" style="left:103px; top:492px;">Straße, Haus-Nr.:</span>
  <div class="field" style="left:334px; top:484px; width:766px;"></div>

  <span class="label" style="left:103px; top:554px;">PLZ, Ort:</span>
  <div class="field" style="left:334px; top:546px; width:766px;"></div>

  <span class="label" style="left:103px; top:614px;">Art der Installation:</span>
  <div class="checkbox" style="left:335px; top:615px;"></div>
  <span class="option" style="left:369px; top:614px;">Oberirdisch</span>
  <div class="checkbox" style="left:553px; top:615px;"></div>
  <span class="option" style="left:583px; top:614px;">Unterirdisch</span>

  <span class="label" style="left:103px; top:667px;">Größe der Rasenfläche:</span>
  <div class="checkbox" style="left:396px; top:668px;"></div>
  <span class="option" style="left:425px; top:667px;">0 bis 250m²</span>
  <div class="checkbox" style="left:580px; top:668px;"></div>
  <span class="option" style="left:614px; top:667px;">251 bis 500m²</span>
  <div class="checkbox" style="left:826px; top:668px;"></div>
  <span class="option" style="left:862px; top:667px;">501 bis 1.000m²</span>

  <span class="label" style="left:315px; top:749px;">Datum:</span>
  <div class="signline" style="left:408px; top:768px; width:250px;"></div>
  <span class="label" style="left:685px; top:749px;">Unterschrift:</span>
  <div class="signline" style="left:839px; top:768px; width:251px;"></div>

  <div class="brand">
    <span class="brand-dot"></span>
    <span class="brand-name">Momentwerk Atelier</span>
  </div>

  <span class="contact contact-line">+49 (0) 6221 480315&nbsp; | &nbsp;info@momentwerk-atelier.de</span>
  <span class="contact contact-web">www.momentwerk-atelier.de</span>
</main>
</body>
</html>
```